New business card with our logo

we finalized our logo with the help of pixel harbor - now we need a business card using that logo. we are a metal service center providing raw steel and metal products for fabricating, contractors, artists, etc. we have the wording for the back of the card figured out (attached, no deviations from text please), just need help putting it all together.
Contact Information for Business Card
would like the look of steel somehow incorporated in the design ... would like the black part of the logo to be steel or silver color (the S & MORROW)
Font styles to use
Other font styles liked:
- calibri, arial, similar to those, modern looking
Colors
Designer to choose colors to be used in the design.
Requirements
Must have
- Back of card must haves are attached (no deviations from wording please).
- FRONT of card:
- logo
- address
- name
- office tel
- cell
- fax
- website
- address
Nice to have
- incorporate the look of steel or element of steel somehow
- names of the staff on front not in all caps, i.e. Tereza not TEREZA
- this industry is more industrial, not coffee or flower shop so design should be aligned with that
- design should be classic and tasteful

```html
<!DOCTYPE html>
<html lang="en">
<head>
<meta charset="utf-8">
<title>Morrow Steel – Business Card</title>
<link href="https://fonts.googleapis.com/css2?family=Lato:ital,wght@0,400;0,700;1,700&family=Roboto:wght@400;500;700&display=swap" rel="stylesheet">
<style>
  :root {
    --bg: #e9e9ec;
    --card-dark: #232325;
    --blue: #1f78c8;
    --blue-deep: #1565b0;
    --ink: #2b2c30;
    --ink-soft: #3c3d42;
    --white: #ffffff;
    --ghost: #eef0f7;
  }
  * { box-sizing: border-box; margin: 0; padding: 0; }
  html, body { width: 1200px; height: 849px; overflow: hidden; }
  body { background: var(--bg); position: relative; font-family: "Roboto", Arial, sans-serif; }

  .card {
    position: absolute;
    left: 262px;
    width: 652px;
    height: 354px;
    border-radius: 18px;
    overflow: hidden;
    box-shadow: 0 6px 14px rgba(0,0,0,.25);
  }

  /* Back of card */
  .card-back { top: 46px; background: var(--card-dark); font-family: "Lato", Arial, sans-serif; color: var(--white); text-align: center; }
  .brand-mark {
    position: absolute; top: 74px; left: 0; width: 100%;
    display: flex; justify-content: center; align-items: center; gap: 14px;
  }
  .brand-mark .dot { width: 30px; height: 30px; border-radius: 50%; background: var(--blue); }
  .brand-mark .name { font-weight: 700; font-size: 36px; letter-spacing: 1px; color: var(--white); }
  .headline { position: absolute; top: 185px; width: 100%; font-size: 29px; font-weight: 700; color: var(--blue); }
  .services { position: absolute; top: 220px; width: 100%; font-size: 19px; }
  .products { position: absolute; top: 259px; width: 100%; font-size: 19px; line-height: 24px; }
  .bullet { color: var(--blue); font-size: 14px; vertical-align: 2px; margin: 0 3px; }
  .tagline { position: absolute; top: 310px; width: 100%; font-size: 20px; font-weight: 700; font-style: italic; color: var(--blue); }

  /* Front of card */
  .card-front { top: 446px; background: var(--white); }
  .ghost-ring {
    position: absolute; left: 361px; top: -7px;
    width: 370px; height: 370px; border-radius: 50%;
    border: 22px solid var(--ghost);
  }
  .front-brand { position: absolute; left: 42px; top: 58px; display: flex; align-items: center; gap: 14px; }
  .front-brand .dot { width: 40px; height: 40px; border-radius: 50%; background: var(--blue); }
  .front-brand .name { font-weight: 700; font-size: 30px; color: var(--ink); letter-spacing: .5px; }

  .person { position: absolute; right: 38px; top: 158px; text-align: right; }
  .person .full-name { font-size: 26px; font-weight: 700; color: var(--blue); line-height: 1.1; }
  .person .role { font-size: 14.5px; color: var(--ink-soft); margin-top: 3px; }
  .divider { position: absolute; left: 0; top: 218px; width: 614px; height: 1.5px; background: var(--blue); }

  .contacts { position: absolute; left: 42px; top: 236px; list-style: none; }
  .contacts li { display: flex; align-items: center; height: 20px; font-size: 14.5px; color: var(--ink); }
  .contacts svg { width: 12px; height: 12px; margin-right: 9px; fill: var(--blue); flex: none; }

  .address { position: absolute; right: 30px; top: 294px; text-align: right; font-size: 14.5px; color: var(--ink); line-height: 20px; }
  .address .line { display: flex; justify-content: flex-end; align-items: center; gap: 7px; }
  .address svg { width: 11px; height: 13px; fill: var(--blue); }
  .address .line.second { margin-right: 18px; }
  .bottom-band { position: absolute; left: 0; bottom: 0; width: 100%; height: 6px; background: var(--blue-deep); }
</style>
</head>
<body>

<section class="card card-back" aria-label="Back of card">
  <div class="brand-mark"><span class="dot"></span><span class="name">MORROW STEEL</span></div>
  <h1 class="headline">Metal Service Center</h1>
  <p class="services">Cut <span class="bullet">●</span> Shear <span class="bullet">●</span> Punch <span class="bullet">●</span> Light Fab</p>
  <p class="products">Structural Steel <span class="bullet">●</span> Stainless &amp; Aluminium<br><span class="bullet">●</span> Building Components <span class="bullet">●</span> Rebar <span class="bullet">●</span> Decking......... and more!</p>
  <p class="tagline">Cut to size, Pick-up or Delivered!</p>
</section>

<section class="card card-front" aria-label="Front of card">
  <div class="ghost-ring"></div>
  <div class="front-brand"><span class="dot"></span><span class="name">MORROW STEEL</span></div>

  <div class="person">
    <div class="full-name">Daniel Varga</div>
    <div class="role">Managing Director</div>
  </div>
  <div class="divider"></div>

  <ul class="contacts">
    <li><svg viewBox="0 0 12 12"><path d="M3 0h6a1 1 0 0 1 1 1v10a1 1 0 0 1-1 1H3a1 1 0 0 1-1-1V1a1 1 0 0 1 1-1zm.5 1.5v8h5v-8z"/></svg>+000 000 0000</li>
    <li><svg viewBox="0 0 12 12"><path d="M2.5 1 4.5 3 3.4 4.6a7 7 0 0 0 4 4L9 7.5l2 2-1.5 1.8C5 11 1 7 .7 2.5z"/></svg>+000 000 0000</li>
    <li><svg viewBox="0 0 12 12"><path d="M3 0h6v3H3zM1 4h10a1 1 0 0 1 1 1v4H10v3H2V9H0V5a1 1 0 0 1 1-1zm2 4v3h6V8z"/></svg>+000 000 0000</li>
    <li><svg viewBox="0 0 12 12"><path d="M0 2h12v1L6 7 0 3zm0 2.5 6 4 6-4V10H0z"/></svg>info@morrowsteel.com</li>
    <li><svg viewBox="0 0 12 12"><circle cx="6" cy="6" r="5.5" fill="none" stroke="#1f78c8" stroke-width="1.2"/><path d="M4 2.5c1.5 1 2 2.5 1 3.5s-1 2 0 4M7 3c1 1 1.5 2 1 3" fill="none" stroke="#1f78c8" stroke-width="1.2"/></svg>www.morrowsteel.com</li>
  </ul>

  <div class="address">
    <div class="line">Harbour Lane 27 <svg viewBox="0 0 11 13"><path d="M5.5 0A5 5 0 0 1 10.5 5c0 3.5-5 8-5 8S.5 8.5.5 5A5 5 0 0 1 5.5 0zm0 3a2 2 0 1 0 0 4 2 2 0 0 0 0-4z"/></svg></div>
    <div class="line second">Halden 2040, Canada</div>
  </div>
  <div class="bottom-band"></div>
</section>

</body>
</html>
```